" Dentista, especialista em Ortodontia. Professor Universitário, com titulaçao de excelência (Doutor). Atua em consultório particular atuando em uma odontologia de excelência, correçao dos dentes através de aparelhos dentários e reabilitaçao oral com técnicas de altíssimo nível em um ambiente diferenciado. Profissional qualificado e bem conceituado no mercado de trabalho. Possui uma logo, feita por um amador, a qual tive a infelicidade de descobrir que foi clonada de um profissional americano. "

```html
<!DOCTYPE html>
<html lang="pt-BR">
<head>
<meta charset="utf-8">
<title>Papel timbrado – Dr. Rafael Monteiro</title>
<link rel="stylesheet" href="https://fonts.googleapis.com/css2?family=Ubuntu:wght@400;500&display=swap">
<style>
  :root {
    --backdrop: #e7e7e5;
    --paper: #ffffff;
    --teal: #4a9ea3;
    --ink: #4b5a5e;
    --ink-dark: #2f4650;
  }
  * { margin: 0; padding: 0; box-sizing: border-box; }
  html, body {
    width: 1200px;
    height: 1200px;
    overflow: hidden;
    background: var(--backdrop);
    font-family: "Ubuntu", sans-serif;
  }
  .letterhead {
    position: absolute;
    left: 210px;
    top: 75px;
    width: 780px;
    height: 1050px;
    background: var(--paper);
    box-shadow: 0 2px 10px rgba(0,0,0,0.15);
  }
  .credentials {
    position: absolute;
    left: 22px;
    top: 50px;
    font-size: 12.5px;
    line-height: 17px;
    color: var(--ink);
    font-weight: 500;
    white-space: nowrap;
  }
  .header-rule {
    position: absolute;
    left: 0;
    top: 100px;
    width: 565px;
    height: 5px;
    background: var(--teal);
  }
  .brand {
    position: absolute;
    right: 20px;
    top: 32px;
    width: 190px;
    text-align: right;
  }
  .brand-mark {
    display: inline-block;
    width: 22px;
    height: 22px;
    border-radius: 50%;
    background: var(--teal);
    margin-bottom: 6px;
  }
  .brand-name {
    font-size: 17px;
    font-weight: 500;
    color: var(--ink-dark);
    line-height: 20px;
    white-space: nowrap;
  }
  .brand-role {
    font-size: 9px;
    letter-spacing: 3.2px;
    color: var(--teal);
    line-height: 13px;
  }
  .brand-registry {
    font-size: 8px;
    color: var(--ink);
    line-height: 12px;
    padding-right: 12px;
  }
  .footer-contact {
    position: absolute;
    left: 0;
    right: 0;
    top: 955px;
    text-align: center;
    font-size: 12px;
    line-height: 19px;
    color: var(--ink);
    font-weight: 500;
  }
  .footer-band {
    position: absolute;
    left: 0;
    right: 0;
    bottom: 18px;
    height: 11px;
    background: var(--teal);
  }
</style>
</head>
<body>
  <main class="letterhead">
    <header>
      <div class="credentials">
        <p>Especialista e Mestre em Ortodontia - Instituto Vértice Azul - Campinas/SP</p>
        <p>Doutor em Odontologia - FOL - Unilumen</p>
      </div>
      <div class="header-rule"></div>
      <div class="brand">
        <span class="brand-mark"></span>
        <p class="brand-name">Dr. Rafael Monteiro</p>
        <p class="brand-role">ORTODONTISTA</p>
        <p class="brand-registry">CRO-SP 00000</p>
      </div>
    </header>
    <footer>
      <div class="footer-contact">
        <p>Av. das Palmeiras, 456 - sala 12 Centro - São Paulo - SP</p>
        <p>11 4000-1234/4000-5678</p>
      </div>
      <div class="footer-band"></div>
    </footer>
  </main>
</body>
</html>
```